Appliance Point of Purchase Campaign

I m looking to create a campaign to be used in an applinace retail store for our extended warranty program. The theme is focused on how much people use thier appliances over the life of the warranty period. As an example, familiesv open thier fridge an average of 40x per day. I habe included a link to a drop box folder which contain our marketing assets as well as a power piint which will give you an idea of hte kind of appliances we wnat to create point of sales pieces for - stickers, posters and pop ups. Hopefully it will be self explanatory. I want prices for a fridge, washer, dishware and range.

here is a link to the folder with the powerpoint overview and some of our marketing assets. Im on a plane to rome and will be able to respond to questons when i land at about 5 AM EST.

https://www.filevarka.net/s/q4mwz7trpa2xn8d/QXbrTmvYHPcLwe9kfsRjUnZo?v=0

Target Market(s)

appliance purchasers. mothers, families

Industry/Entity Type

Appliance

Colors
33a6d7
33b8a4

Requirements
Must have
• include ideas for fridge, range, dishwasher and washer. Multiple ideas for impactful point of purchase materials that will spark discussion between a sales person and the customers
• This campaign is to drive customers to
Nice to have
• images can include real life things that might be in an appliance - dishes, ice, food etc.
• Improved copywriting with clear concise messaging
• Use our brand guidelines that are in the Dropbox folder.

```html
<!DOCTYPE html>
<html lang="en">
<head>
<meta charset="utf-8">
<title>Range Sticker – 1,000 Meals</title>
<link href="https://fonts.googleapis.com/css2?family=Montserrat:wght@500;600;700&display=swap" rel="stylesheet">
<style>
  :root {
    --teal: #33b8a4;
    --white: #ffffff;
    --backdrop: #eceeee;
    --photo-dark: #1f2224;
    --photo-mid: #3a3f42;
    --photo-warm: #b5533f;
  }
  * { margin: 0; padding: 0; box-sizing: border-box; }
  html, body {
    width: 1200px;
    height: 914px;
    overflow: hidden;
    background: var(--backdrop);
  }
  .canvas {
    position: relative;
    width: 1200px;
    height: 914px;
    font-family: "Montserrat", sans-serif;
  }
  .sticker-shape {
    position: absolute;
    left: 0;
    top: 0;
  }
  .stat-number {
    position: absolute;
    left: 0;
    width: 1200px;
    top: 200px;
    text-align: center;
    font-size: 94px;
    font-weight: 600;
    letter-spacing: -2px;
    line-height: 1;
    color: var(--white);
  }
  .stat-message {
    position: absolute;
    left: 347px;
    top: 326px;
    width: 300px;
    font-size: 18px;
    font-weight: 600;
    line-height: 25px;
    color: var(--white);
  }
  .plan-mark {
    position: absolute;
    left: 680px;
    top: 348px;
    display: flex;
    align-items: center;
    gap: 10px;
  }
  .plan-mark-dot {
    width: 16px;
    height: 16px;
    border-radius: 50%;
    background: var(--white);
  }
  .plan-mark-name {
    font-size: 17px;
    font-weight: 500;
    line-height: 20px;
    color: var(--white);
  }
</style>
</head>
<body>
  <main class="canvas">
    <svg class="sticker-shape" width="1200" height="914" viewBox="0 0 1200 914" xmlns="http://www.w3.org/2000/svg">
      <defs>
        <clipPath id="upper-half">
          <rect x="0" y="0" width="1200" height="453"/>
        </clipPath>
        <clipPath id="lower-window">
          <rect x="0" y="475" width="1200" height="439"/>
        </clipPath>
        <linearGradient id="meal-tones" x1="0" y1="0" x2="1" y2="1">
          <stop offset="0" stop-color="var(--photo-warm)"/>
          <stop offset="0.45" stop-color="var(--photo-mid)"/>
          <stop offset="1" stop-color="var(--photo-dark)"/>
        </linearGradient>
      </defs>
      <circle class="sticker-base" cx="600" cy="457" r="330" fill="var(--white)"/>
      <circle class="sticker-header" cx="600" cy="457" r="330" fill="var(--teal)" clip-path="url(#upper-half)"/>
      <g clip-path="url(#lower-window)">
        <circle class="sticker-photo" cx="600" cy="457" r="305" fill="url(#meal-tones)"
                role="img" aria-label="Photo of chicken and cherry tomato skewers with lemon slices in a dark frying pan"/>
      </g>
    </svg>

    <div class="stat-number">1,000</div>
    <p class="stat-message">The number of meals average family cooks in a year. Protect me with the Appliance Protection Plan.</p>

    <div class="plan-mark">
      <span class="plan-mark-dot"></span>
      <span class="plan-mark-name">Hearthwise<br>Care Plan</span>
    </div>
  </main>
</body>
</html>
```